NEED A COOL QUICK SIIMPLE FLYER FOR A HOT SHAVE ICE BIZ!

DOING WELL ON SOCIAL MEDIA, NEED TO PASS OUT A 1 PAGE FLYER AROUND TOWN SO MORE PEOPLE KNOW WHERE WE ARE. I WANT IT TO BE INFORMATIVE YET CREATIVE AND POP! THIS IS KINDA LAST MINUTE BUT WANT TO TRY TO GET OUT FOR WEEKEND. PLEASE READ THE MUST HAVES...OPEN TO MANY IDEAS...USE MY UPLOADS TO CREATE. FLYER IS 8.5X11"

Target Market(s)

HANDED OUT IN PARKING LOTS AND BUSINESSES

Industry/Entity Type

Town

Font styles to use
Serif

Requirements
Must have
• IF YOU CAN DECIPHER MY MAP LOL...WOULD LIKE TO HAVE THE MAP. THE MAP NEEDS TO SAY "ON THE CORNER OF 7TH AND 11TH ION LINDENVALE BY PLUM!" AD THE MENU IF POSSIBLE OR PARTS OF IT..I WOULD LIKE TO ADD SOCIAL MEDIA LOGOS LIKE "FIND US ON CHATTERBOX" AND "FOLLOW US ON SNAPLOOP" @BREEZYPEAK. USE SAME COLOR SCHEME AS OUR LOGO. NEEDS TO INCLUDE THE FOLLOWING VERBIAGE..HOWEVER YOU WANT TO PLACE IT. GENUINE HAWAIIAN SHAVE ICE! NOW OPEN! ICE SHAVED RIGHT OFF THE BLOCK! WE ARE OPEN FROM 1PM TO 8 PM M-F AND 2PM TO 7PM SUNDAY. READ OUR REVIEWS ON CHATTERBOX..WE ARE AN AWESOME PLACE TO CHILL!" NEEDS A PROMINENT STAR BURST OR SOMETHING SAYING DRIVE-THRU AND WALK-UP!" ADD OUR WEBSITE WWW.BREEZYPEAK.EXAMPLE
Nice to have
• NOT TOO CLUTTERED..HOPE I DIDN'T OVER DO THE ABOVE MUST HAVES...PLEASE EMAIL ME WITH QUESTIONS..I WILL GET BACK ASAP...I HAVE DONE A LOT ON SKETCH HIVE I PAY ASAP.
Should not have
• OVER CLUTTERED AND HARD TO READ..SIMPLE LIKE OUR MENU

```html
<!DOCTYPE html>
<html lang="en">
<head>
<meta charset="utf-8">
<title>Breezy Peak Shave Ice – Now Open</title>
<link rel="stylesheet" href="https://fonts.googleapis.com/css2?family=Alfa+Slab+One&family=Libre+Baskerville:wght@400;700&family=Montserrat:wght@400;800&family=Roboto+Condensed:wght@400&display=swap">
<style>
  :root{
    --red:#e8434a;
    --deep-red:#c8151d;
    --blue:#1ea3e3;
    --yellow:#ffe84a;
    --gold:#f6c343;
    --black:#111111;
    --white:#ffffff;
    --map:#e8e9e9;
    --green:#5bbf3a;
  }
  *{box-sizing:border-box;margin:0;padding:0}
  html,body{width:928px;height:1200px;overflow:hidden;background:var(--white)}
  .flyer{position:relative;width:928px;height:1200px;overflow:hidden;background:var(--white);font-family:"Libre Baskerville",Georgia,serif;color:var(--black)}
  .photo{position:absolute;left:0;top:225px;width:928px;height:921px;
    background:
      radial-gradient(ellipse 260px 300px at 470px 560px, #f3e25a 0%, #f1c93a 45%, rgba(241,201,58,0) 100%),
      radial-gradient(ellipse 230px 200px at 120px 800px, #7fd14a 0%, var(--green) 50%, rgba(91,191,58,0) 100%),
      radial-gradient(ellipse 420px 420px at 330px 360px, #f24a55 0%, #e0222e 60%, rgba(224,34,46,0) 100%),
      linear-gradient(160deg,#d8141c 0%,#b90e15 60%,#8f0a10 100%);}
  .shapes{position:absolute;left:0;top:0;width:928px;height:1200px}
  .abs{position:absolute}
  .brand-name{left:20px;top:150px;width:260px;text-align:center;font-weight:700;font-size:30px;color:var(--deep-red)}
  .tagline{left:446px;top:178px;font-size:27px;white-space:nowrap}
  .tagline b{font-weight:700}
  .chill-line{left:140px;top:240px;width:700px;text-align:center;font-size:25px;color:var(--white);letter-spacing:.5px;transform:rotate(-1.3deg);white-space:nowrap}
  .chill-line b{color:var(--yellow);font-weight:700}
  .now-open{width:126px;text-align:center;font-size:23px;line-height:1.1}
  .now-open b{font-weight:700}
  .price{width:124px;text-align:center;color:var(--black)}
  .price .size{font-weight:700;font-size:16px;letter-spacing:.3px}
  .price .cost{font-weight:700;font-size:32px;color:var(--deep-red);line-height:1.05}
  .price sup{font-size:15px;vertical-align:top;position:relative;top:4px}
  .try{left:60px;top:466px;width:240px;text-align:center}
  .try .big{font-family:"Alfa Slab One",Georgia,serif;font-size:70px;line-height:.95;letter-spacing:1px}
  .try .red{color:var(--red);font-family:"Montserrat",Arial,sans-serif;font-size:13px;margin-top:6px}
  .try .dark{font-family:"Montserrat",Arial,sans-serif;font-weight:800;font-size:13px;margin-top:6px}
  .try .tops{font-family:"Montserrat",Arial,sans-serif;font-weight:800;font-size:23px}
  .flavors{left:36px;top:652px;width:236px;text-align:center;color:var(--white);font-family:"Montserrat",Arial,sans-serif}
  .flavors .over{font-weight:800;font-size:27px;color:var(--yellow)}
  .flavors .fifty{font-family:"Libre Baskerville",Georgia,serif;font-size:96px;line-height:.95;color:var(--yellow);-webkit-text-stroke:2px var(--black)}
  .flavors .small{font-size:15px;font-weight:800;line-height:1.35}
  .flavors .small span{font-weight:400}
  .hours{left:626px;top:812px;width:184px;text-align:center;color:var(--white)}
  .hours .open{font-family:"Alfa Slab One",Georgia,serif;font-size:52px;color:var(--red);line-height:1}
  .hours .line{font-family:"Montserrat",Arial,sans-serif;font-weight:800;font-size:16px;line-height:1.4}
  .drive{left:18px;top:1106px;font-family:"Alfa Slab One",Georgia,serif;font-size:29px;color:var(--yellow);-webkit-text-stroke:1px var(--deep-red);white-space:nowrap}
  .drive span{font-family:"Montserrat",Arial,sans-serif;font-weight:400;font-size:18px;color:var(--black);-webkit-text-stroke:0;margin:0 4px}
  .reviews-strip{left:0;top:1146px;width:928px;height:24px;background:var(--yellow)}
  .reviews{left:74px;top:1150px;font-family:"Montserrat",Arial,sans-serif;font-weight:800;font-size:13px}
  .reviews span{font-weight:400}
  .footer{left:0;top:1170px;width:928px;height:30px;background:var(--white)}
  .social-square{left:20px;top:1176px;width:18px;height:18px;background:var(--red)}
  .follow{left:46px;top:1178px;font-family:"Montserrat",Arial,sans-serif;font-size:12.5px;white-space:nowrap}
  .website{left:252px;top:1176px;width:286px;font-weight:700;font-size:14.5px;color:var(--deep-red);letter-spacing:.2px;white-space:nowrap}
  .location{left:546px;top:1170px;width:382px;height:30px;background:var(--black);color:var(--white);font-family:"Montserrat",Arial,sans-serif;font-weight:800;font-size:11px;line-height:30px;text-align:center;white-space:nowrap}
</style>
</head>
<body>
<main class="flyer">
  <div class="photo" role="img" aria-label="Close-up photo of a rainbow shave ice in red, yellow and green syrup in a green cup with a purple straw"></div>

  <svg class="shapes" viewBox="0 0 928 1200">
    <defs>
      <symbol id="burst" viewBox="0 0 100 100" preserveAspectRatio="none">
        <polygon points="100,50 93.2,58.6 96.2,69.1 86.6,74.5 85.4,85.4 74.5,86.6 69.1,96.2 58.6,93.2 50,100 41.4,93.2 30.9,96.2 25.5,86.6 14.6,85.4 13.4,74.5 3.8,69.1 6.8,58.6 0,50 6.8,41.4 3.8,30.9 13.4,25.5 14.6,14.6 25.5,13.4 30.9,3.8 41.4,6.8 50,0 58.6,6.8 69.1,3.8 74.5,13.4 85.4,14.6 86.6,25.5 96.2,30.9 93.2,41.4"/>
      </symbol>
    </defs>

    <rect class="header-bg" x="0" y="0" width="928" height="226" fill="var(--white)"/>
    <circle class="brand-circle" cx="150" cy="82" r="62" fill="var(--gold)"/>
    <text x="294" y="78" textLength="588" lengthAdjust="spacingAndGlyphs" font-family="Montserrat, Arial, sans-serif" font-size="50" fill="var(--black)">GENUINE <tspan font-weight="800">HAWAIIAN</tspan></text>
    <text x="294" y="172" textLength="360" lengthAdjust="spacingAndGlyphs" font-family="Roboto Condensed, Arial, sans-serif" font-size="128" fill="var(--red)">SHAVE</text>
    <text x="672" y="172" textLength="210" lengthAdjust="spacingAndGlyphs" font-family="Roboto Condensed, Arial, sans-serif" font-size="128" fill="var(--blue)">ICE!</text>

    <polygon class="chill-banner" points="0,248 928,222 928,272 0,298" fill="var(--black)"/>

    <ellipse cx="68" cy="274" rx="62" ry="44" fill="var(--yellow)" stroke="var(--black)" stroke-width="2"/>
    <ellipse cx="866" cy="238" rx="58" ry="44" fill="var(--yellow)" stroke="var(--black)" stroke-width="2"/>

    <use href="#burst" x="606" y="324" width="120" height="110" fill="var(--white)"/>
    <use href="#burst" x="680" y="420" width="120" height="110" fill="var(--white)"/>
    <use href="#burst" x="700" y="542" width="132" height="112" fill="var(--white)"/>

    <use href="#burst" x="44" y="446" width="272" height="188" fill="var(--white)"/>
    <use href="#burst" x="24" y="630" width="262" height="200" fill="var(--red)"/>

    <g role="img" aria-label="Street map of the corner of 7th and 11th with the shop marked next to Plum">
      <circle cx="792" cy="1116" r="272" fill="var(--map)"/>
    </g>

    <polygon class="hours-sign" points="626,806 810,806 810,910 730,910 718,922 706,910 626,910" fill="var(--black)"/>
  </svg>

  <div class="abs brand-name">Breezy Peak</div>
  <p class="abs tagline"><b>Shaved</b> right of the block!</p>
  <p class="abs chill-line">WE ARE AN <b>AWESOME PLACE</b> TO CHILL!</p>

  <p class="abs now-open" style="left:6px;top:248px">NOW<br><b>OPEN!</b></p>
  <p class="abs now-open" style="left:804px;top:212px">NOW<br><b>OPEN!</b></p>

  <div class="abs price" style="left:604px;top:354px"><div class="size">KIDDIE</div><div class="cost">2.<sup>95</sup></div></div>
  <div class="abs price" style="left:678px;top:450px"><div class="size">LARGE</div><div class="cost">3.<sup>95</sup></div></div>
  <div class="abs price" style="left:704px;top:573px"><div class="size">REGULAR</div><div class="cost">4.<sup>95</sup></div></div>

  <div class="abs try">
    <div class="big">TRY</div>
    <div class="red">ICE CREAM IN THE MIDDLE!</div>
    <div class="dark">OR SOME OF OUR FAVORITE</div>
    <div class="tops">TOPPINGS!</div>
  </div>

  <div class="abs flavors">
    <div class="over">OVER</div>
    <div class="fifty">50</div>
    <div class="small">FLAVORS <span>TO</span><br><span>CHOOSE FROM!</span></div>
  </div>

  <div class="abs hours">
    <div class="open">OPEN</div>
    <div class="line">1PM - 8PM Mon-Sat</div>
    <div class="line">2PM - 7PM Sunday</div>
  </div>

  <p class="abs drive">DRIVE-THRU<span>and</span>WALK-UP!</p>

  <div class="abs reviews-strip"></div>
  <p class="abs reviews"><span>READ OUR</span> REVIEWS <span>ON</span> CHATTERBOX</p>
  <div class="abs footer"></div>
  <div class="abs social-square"></div>
  <p class="abs follow">FOLLOW US: @BREEZYPEAK</p>
  <p class="abs website">WWW.BREEZYPEAK.EXAMPLE</p>
  <p class="abs location">ON THE CORNER OF 7TH AND 11TH ION LINDENVALE BY PLUM</p>
</main>
</body>
</html>
```